Global Expert Network Firm needs business card design

We need business card design for a new company based in Seoul, South Korea called 'Corwell Insight Partners'. We recruit industry experts covering all countries and connect our client and recruited expert by phone, face-to-face meetings and etc. We are a global expert network firm that is focused on delivering high-quality experts to our clients throughout the world. Our clients include multinational corporations, global consulting firms, private equity firms, venture capital firms, asset management companies.
We have made new logo and please find attachment.(Please use new logo)
Target Market(s)
Global Consulting Firms, Investment Firms, Private Equity Firms, Venture Capital Firms.
Industry/Entity Type
Recruitment
Contact Information for Business Card
We need two Languages (English and Korean Version).
The front is Korean and the back is English version.
[The back] [English]
Company Name: Corwell Insight Partners, Inc.
CEO Name: Daniel Park
Address: #507, Hanbit Bldg, 82 Maebongsan-ro, Dobong-gu, Seoul, 01327, Korea
Tel. +82 2 718 4052
Fax. +82 2 864 1097
Mobile. +82 10 7264 8815
Email: daniel@corwellip.com
Web: www.corwellip.com
[The front] [Korean] => Described in same order as English version.
회사명: 코웰인사이트파트너스(주)
대표이사: 박도현
주소: 서울시 도봉구 매봉산로 82 한빛빌딩 507호
Tel. 02 718 4052
Fax. 02 864 1097
Mobile. 010 7264 8815
Web: www.corwellip.com
Look and feel
Each slider illustrates characteristics of the customer's brand and the style your logo design should communicate.

```html
<!DOCTYPE html>
<html lang="ko">
<head>
<meta charset="utf-8">
<title>Corwell Insight Partners – Business Card</title>
<link rel="stylesheet" href="https://fonts.googleapis.com/css2?family=Noto+Sans+KR:wght@300;400;700&family=Open+Sans:wght@300;400;700&display=swap">
<style>
  :root {
    --backdrop: #2b2b2d;
    --navy: #1b2150;
    --paper: #f1f1f1;
    --ink-on-paper: #26284a;
    --ink-on-navy: #ffffff;
  }
  * { margin: 0; padding: 0; box-sizing: border-box; }
  html, body { width: 1200px; height: 960px; overflow: hidden; }
  body {
    background: var(--backdrop);
    position: relative;
    font-family: "Open Sans", "Noto Sans KR", sans-serif;
  }
  .card {
    position: absolute;
    width: 600px;
    height: 342px;
    display: flex;
    box-shadow: 0 3px 8px rgba(0,0,0,.45);
  }
  .card--front { left: 321px; top: 108px; }
  .card--back  { left: 320px; top: 493px; }

  .panel { height: 100%; position: relative; }
  .panel--info { width: 273px; padding-left: 33px; }
  .panel--brand { flex: 1; display: flex; align-items: center; padding-left: 60px; }

  .panel--paper { background: var(--paper); color: var(--ink-on-paper); }
  .panel--navy  { background: var(--navy);  color: var(--ink-on-navy); }

  .brand-name {
    font-family: "Open Sans", sans-serif;
    font-weight: 300;
    font-size: 36px;
    line-height: 66px;
    letter-spacing: 0.5px;
  }

  .kr { font-family: "Noto Sans KR", sans-serif; font-weight: 400; }
  .company-kr { margin-top: 55px; font-size: 16px; line-height: 22px; }
  .person-kr  { font-size: 16px; line-height: 22px; }
  .address    { font-size: 14.5px; line-height: 19.5px; }
  .address--kr { margin-top: 17px; }

  .person-en {
    margin-top: 52px;
    font-weight: 700;
    font-size: 18px;
    line-height: 22px;
    letter-spacing: -0.4px;
  }
  .role { font-weight: 700; font-size: 13px; line-height: 16px; margin-left: 2px; }
  .address--en { margin-top: 18px; }

  .contacts { list-style: none; margin-top: 8px; }
  .contacts li {
    display: flex;
    align-items: center;
    height: 19.7px;
    font-size: 14px;
  }
  .contacts svg { width: 14px; height: 14px; margin-right: 9px; flex: none; fill: currentColor; }
</style>
</head>
<body>

<!-- Front: Korean -->
<section class="card card--front">
  <div class="panel panel--info panel--paper">
    <p class="kr company-kr">코웰인사이트파트너스(주)</p>
    <p class="kr person-kr">박도현</p>
    <p class="kr address address--kr">서울시 도봉구<br>매봉산로 82<br>한빛빌딩 507호</p>
    <ul class="contacts">
      <li><svg viewBox="0 0 14 14"><path d="M1 4c0-2 2.5-3 6-3s6 1 6 3v1.5h-3V4H4v1.5H1z M3 6.5h8l1.5 6.5h-11z"/></svg>+82 2 718 4052</li>
      <li><svg viewBox="0 0 14 14"><path d="M4 0h6a1 1 0 0 1 1 1v12a1 1 0 0 1-1 1H4a1 1 0 0 1-1-1V1a1 1 0 0 1 1-1zm.5 2v8.5h5V2zM7 11.3a.9.9 0 1 0 0 1.8.9.9 0 0 0 0-1.8z"/></svg>+82 2 864 1097</li>
      <li><svg viewBox="0 0 14 14"><path d="M3 1h8v4H3z M1 6h12v7H1z M3 10h8v1.5H3z" /></svg>+82 10 7264 8815</li>
      <li><svg viewBox="0 0 14 14"><path d="M1 3h12v1L7 8 1 4z M1 5.5l6 4 6-4V11H1z"/></svg>daniel@corwellip.com</li>
      <li><svg viewBox="0 0 14 14"><circle cx="7" cy="7" r="6.3"/></svg>www.corwellip.com</li>
    </ul>
  </div>
  <div class="panel panel--brand panel--navy">
    <p class="brand-name">Corwell<br>Insight<br>Partners</p>
  </div>
</section>

<!-- Back: English -->
<section class="card card--back">
  <div class="panel panel--info panel--navy">
    <p class="person-en">DANIEL PARK</p>
    <p class="role">CEO</p>
    <p class="address address--en">#507, Hanbit Bldg<br>82 Maebongsan-ro<br>Dobong-gu, Seoul<br>01327, Korea</p>
    <ul class="contacts">
      <li><svg viewBox="0 0 14 14"><path d="M1 4c0-2 2.5-3 6-3s6 1 6 3v1.5h-3V4H4v1.5H1z M3 6.5h8l1.5 6.5h-11z"/></svg>+82 2 718 4052</li>
      <li><svg viewBox="0 0 14 14"><path d="M4 0h6a1 1 0 0 1 1 1v12a1 1 0 0 1-1 1H4a1 1 0 0 1-1-1V1a1 1 0 0 1 1-1zm.5 2v8.5h5V2zM7 11.3a.9.9 0 1 0 0 1.8.9.9 0 0 0 0-1.8z"/></svg>+82 2 864 1097</li>
      <li><svg viewBox="0 0 14 14"><path d="M3 1h8v4H3z M1 6h12v7H1z M3 10h8v1.5H3z" /></svg>+82 10 7264 8815</li>
      <li><svg viewBox="0 0 14 14"><path d="M1 3h12v1L7 8 1 4z M1 5.5l6 4 6-4V11H1z"/></svg>daniel@corwellip.com</li>
      <li><svg viewBox="0 0 14 14"><circle cx="7" cy="7" r="6.3"/></svg>www.corwellip.com</li>
    </ul>
  </div>
  <div class="panel panel--brand panel--paper">
    <p class="brand-name">Corwell<br>Insight<br>Partners</p>
  </div>
</section>

</body>
</html>
```